Business Card Design Project

Bold, modern, clean business card design needed. Prefer double sided with art logo on the back. Front of card with company name logo, no art.

Target Market(s)

Our consulting company supports local, state and federal law enforcement officers. Therefore the design should be clean and direct with no flash or arrogance to it.

Industry/Entity Type

Business

```html
<!DOCTYPE html>
<html lang="en">
<head>
<meta charset="utf-8">
<title>Halvern Consulting – Business Card</title>
<link rel="stylesheet" href="https://fonts.googleapis.com/css2?family=Open+Sans:wght@400;700&display=swap">
<style>
  :root {
    --page-bg: #e9e6e1;
    --card-top: #c3e84f;
    --card-bottom: #5aa80e;
    --ink: #161a12;
    --ink-soft: #26301a;
    --card-shadow: rgba(40, 30, 20, 0.28);
  }
  * { box-sizing: border-box; margin: 0; padding: 0; }
  html, body { width: 1200px; height: 913px; overflow: hidden; }
  body {
    background: var(--page-bg);
    font-family: "Open Sans", Arial, sans-serif;
    color: var(--ink);
    display: flex;
    align-items: center;
    justify-content: center;
    gap: 48px;
  }
  .card {
    width: 525px;
    height: 300px;
    border-radius: 3px;
    background: linear-gradient(180deg, var(--card-top) 0%, #a3d63a 45%, var(--card-bottom) 100%);
    box-shadow: 0 10px 26px var(--card-shadow);
    position: relative;
  }
  /* Front: company name only */
  .card-front {
    display: flex;
    align-items: center;
    justify-content: center;
    gap: 14px;
  }
  .brand-mark {
    width: 26px; height: 26px;
    border-radius: 50%;
    background: var(--ink);
    flex: none;
  }
  .brand-name {
    font-weight: 700;
    font-size: 32px;
    letter-spacing: 0.08em;
    text-transform: uppercase;
    color: var(--ink);
  }
  /* Back: art area + contact details */
  .card-back { display: flex; align-items: center; }
  .art-area {
    position: absolute;
    left: 62px; top: 88px;
    width: 170px; height: 170px;
    border-radius: 50%;
    background: var(--ink);
  }
  .contact {
    position: absolute;
    left: 290px; top: 62px;
    color: var(--ink);
  }
  .contact-name { font-weight: 700; font-size: 15px; line-height: 1.2; }
  .contact-title { font-size: 10px; margin-bottom: 30px; }
  .contact-list { list-style: none; font-size: 11px; line-height: 1.55; }
  .contact-list li { display: flex; align-items: center; gap: 8px; }
  .contact-list svg { width: 10px; height: 10px; fill: var(--ink-soft); flex: none; }
  .contact-list .web { font-weight: 700; }
  .fax { display: inline-flex; align-items: center; gap: 5px; margin-left: 6px; }
</style>
</head>
<body>
  <section class="card card-front" aria-label="Card front">
    <span class="brand-mark"></span>
    <span class="brand-name">Halvern Consulting</span>
  </section>

  <section class="card card-back" aria-label="Card back">
    <div class="art-area" role="img" aria-label="Brand mark area"></div>
    <div class="contact">
      <p class="contact-name">Your Long Name</p>
      <p class="contact-title">Managing Director</p>
      <ul class="contact-list">
        <li>
          <svg viewBox="0 0 10 10"><path d="M5 0a3.5 3.5 0 0 0-3.5 3.5C1.5 6 5 10 5 10s3.5-4 3.5-6.5A3.5 3.5 0 0 0 5 0zm0 5a1.4 1.4 0 1 1 0-2.8A1.4 1.4 0 0 1 5 5z"/></svg>
          Your Commercial or office address
        </li>
        <li>
          <svg viewBox="0 0 10 10"><path d="M2 1h2l1 2.4-1.3.9a5.5 5.5 0 0 0 2 2l.9-1.3L9 6v2a1 1 0 0 1-1 1A8 8 0 0 1 1 2a1 1 0 0 1 1-1z"/></svg>
          00.00.00.0000
          <span class="fax">
            <svg viewBox="0 0 10 10"><path d="M2 0h5v3H2zM0 4h10v5H0zm2 2v1h6V6z"/></svg>
            00.00.00.0000
          </span>
        </li>
        <li>
          <svg viewBox="0 0 10 10"><path d="M0 2h10v6H0zm1 1v.3l4 2.5 4-2.5V3z"/></svg>
          yourname@yourwebsite.com
        </li>
        <li class="web">
          <svg viewBox="0 0 10 10"><circle cx="5" cy="5" r="4.5"/></svg>
          www.yourwebsite.com
        </li>
      </ul>
    </div>
  </section>
</body>
</html>
```